International Property Consultancy

Brief Overview:

I need a dynamic and well designed website that is easy to use and understand. It has to be unique and different to generic templates that most websites seem to be these days. PLEASE NO GENERIC TEMPLATES FROM THE INTERNET.

Our business has 10 years experience working on struggling international developments that we then work in-house for to turn around and brings bout success. We stay within a project often for long periods of time until success is achieved. We are unique in our approach and completely different to the standard routes to market for many developments. The site is for developers to see what we have done in regards to previous projects, as such we want to incorporate video into this site with a strong design aesthetic. There will be videos of the past projects we have worked on, which will act as case studies.

I like very simple but punchy websites, that people can navigate and understand very easily. Also a big fan of unique and well thought out design aesthetic.

Initial Site layout thoughts:

1) Homepage:
2) About Us
3) What we've done / Work
This part has the projects we have worked on (France, Portugal, London, Morocco). Each one will have some video content and photo images, but also would be good to have a succinct way to mention what we did and the successes in a clever and punchy way.

4) Contact Us

* This is just a guideline. Would be open to input and creative direction on your own part.

*More details and websites we like can be seen in the brief doc attached.

PLEASE VIEW THE WIREFRAME WORD DOC ATTACHED.

Here there are also some more examples to help:

Here are just a few examples of websites and what I like about them:

- www.velmoro.com (clean, nice geometric design aesthetic, good animation when loading and changing pages well thought out all though also coulee be considered a bit dull and basic after the initial homepage slide)
- https://www.farbridgehub.net (Clean site, quite clinical, lacks video content and doesn't engage greatly).
- https://ruskotile.com (minimal, and like how it mixes the design aesthetic more with video and photo content)

- https://www.amberquillworks.com (like the layout of this and how it displays the projects and work section)

- https://brisk.com (Good use of video content)

- https://loomfield.studio (minimal to the point and mixes design with video and animation etc...)

Here is another couple of cool websites that may help give you some direction: https://halvenquay.com www.brisk.com

Hi there, One of the things I thought would be good on the homepage is to add the logo with a 'digital landscape' before flicking down into a slide with video content of the projects... Just an idea but have posted some pics in the brief. We would get this animated for the site. But if you have better ideas, please do run with them. Thanks,

Target Market(s)

Property developers

Number of Pages Required

4 page

Font styles to use
Other font styles liked:
• Read brief

Requirements
Must have
• Needs to be clean, dynamic and easy to follow on desktop and mobile. We will use it as a kind of portfolio website so will need to embed video of past projects we have worked on.

Read brief in docs.
Nice to have
• Clean
Should not have
• Not be another generic template website.
Not have random property stock photos. (We are not a property agency).

```html
<!DOCTYPE html>
<html lang="en">
<head>
<meta charset="utf-8">
<title>Corvanta — International Property Consultancy</title>
<link href="https://fonts.googleapis.com/css2?family=Red+Hat+Display:wght@400;500&family=Lato:wght@400;700&display=swap" rel="stylesheet">
<style>
:root{
  --teal:#133f52;
  --blush:#f8e1da;
  --ink:#14202a;
  --ink-soft:#1b2b36;
  --white:#ffffff;
  --text-dark:#1b2a33;
  --text-muted:#7d7570;
  --accent:#1f5a6c;
}
*{margin:0;padding:0;box-sizing:border-box}
html,body{width:1200px;height:4289px;overflow:hidden}
body{position:relative;font-family:'Lato',sans-serif;background:var(--ink);color:var(--text-dark)}
.abs{position:absolute}
.heading{font-family:'Red Hat Display',sans-serif;font-weight:400}
.eyebrow{font-family:'Lato',sans-serif;font-size:11px;letter-spacing:.06em;text-transform:uppercase;display:flex;align-items:center;gap:8px}
.eyebrow::after{content:"";width:18px;height:3px;border-radius:2px;background:currentColor;opacity:.6}

/* hero */
.hero{left:0;top:0;width:1200px;height:568px;background:linear-gradient(110deg,#8a6a52 0%,#b79a82 30%,#6e5446 60%,#3a2e2a 100%)}
.logo{left:0;top:20px;width:1200px;text-align:center;color:var(--white);font-family:'Red Hat Display',sans-serif;font-size:30px;font-weight:400;letter-spacing:.01em}
.menu-dots{left:1155px;top:26px;width:6px}
.menu-dots span{display:block;width:4px;height:4px;border-radius:50%;background:var(--white);margin-bottom:5px}
.social{display:flex;flex-direction:column;gap:29px;align-items:center;width:14px}
.social .dot{width:10px;height:10px;border-radius:50%;background:var(--white)}
.scroll{left:1146px;top:462px;width:24px;height:70px;color:var(--white)}
.scroll .bar{position:absolute;left:11px;top:0;width:3px;height:16px;background:var(--white)}
.scroll .label{position:absolute;left:-14px;top:44px;transform:rotate(-90deg);font-size:10px;letter-spacing:.08em;width:50px}

/* about */
.about{left:0;top:568px;width:1200px;height:925px;background:var(--teal);color:var(--white)}
.about .eyebrow{position:absolute;left:117px;top:90px;color:#c7d3d8}
.about h1{position:absolute;left:117px;top:116px;font-size:39px;line-height:45px;width:740px}
.photo{background:linear-gradient(160deg,#eeeeec,#d9d4cd 55%,#8b6d5a);box-shadow:0 8px 22px rgba(0,0,0,.18)}
.about .photo{left:117px;top:339px;width:391px;height:491px}
.about h2{position:absolute;left:609px;font-size:36px}
.about .who-title{top:412px}
.about p{position:absolute;left:609px;width:470px;font-size:13px;line-height:22.7px}
.about .who{top:477px}
.about .how-title{top:656px;opacity:.55}
.about .how{top:722px;opacity:.45;height:70px;overflow:hidden;-webkit-mask-image:linear-gradient(#000 40%,transparent)}

/* work */
.work{left:0;top:1493px;width:1200px;height:2222px;background:var(--blush)}
.work > .eyebrow{position:absolute;left:117px;top:92px;color:var(--text-muted)}
.work h2.lead{position:absolute;left:117px;top:118px;font-size:39px;line-height:47px;color:var(--text-dark)}
.work h2.lead a{color:var(--accent);text-decoration:underline;text-decoration-thickness:2px;text-underline-offset:5px}
.project .photo{position:absolute;width:391px;height:491px}
.project .info{position:absolute;width:480px}
.project .eyebrow{color:var(--text-muted)}
.project h3{font-family:'Red Hat Display',sans-serif;font-weight:400;font-size:30px;line-height:38px;margin-top:14px;color:var(--text-dark)}
.place{display:flex;align-items:center;gap:8px;margin-top:8px;font-size:11px;letter-spacing:.06em;color:var(--accent);text-transform:uppercase}
.project p{margin-top:22px;font-size:12.5px;line-height:22.7px;color:var(--text-muted)}
.btn{display:inline-block;margin-top:32px;width:151px;height:37px;border:2px solid var(--accent);border-radius:20px;text-align:center;line-height:33px;font-size:11px;letter-spacing:.06em;color:var(--accent);text-transform:uppercase}
.view{position:absolute;left:356px;top:239px;width:52px;height:52px;border-radius:50%;background:rgba(31,90,108,.75);border:2px solid var(--white);color:var(--white);font-size:9px;text-align:center;line-height:48px;text-transform:uppercase}
.more{left:0;top:2123px;width:1200px;text-align:center;font-size:36px;color:var(--accent);display:flex;justify-content:center;align-items:center;gap:16px}

/* footer */
.footer{left:0;top:3715px;width:1200px;height:574px;background:var(--ink);color:var(--white)}
.footer nav{position:absolute;left:0;top:36px;width:1200px;display:flex;justify-content:center;gap:52px;font-size:11px;letter-spacing:.06em;text-transform:uppercase}
.wordmark{left:0;top:145px;width:1200px;text-align:center;font-family:'Red Hat Display',sans-serif;font-size:215px;color:var(--ink-soft);line-height:1}
.copy{left:0;top:520px;width:1200px;text-align:center;font-size:10.5px;letter-spacing:.06em}
.totop{left:1146px;top:427px;width:24px;height:130px}
.totop .bar{position:absolute;left:11px;top:0;width:3px;height:16px;background:var(--white)}
.totop .label{position:absolute;left:-30px;top:80px;transform:rotate(-90deg);font-size:10px;letter-spacing:.08em;width:84px;text-transform:uppercase}
</style>
</head>
<body>

<header class="hero abs" role="img" aria-label="Photo of a team of consultants reviewing documents around a meeting table"></header>
<div class="logo abs">corvanta.</div>
<div class="menu-dots abs"><span></span><span></span><span></span></div>
<div class="social abs" style="left:31px;top:384px">
  <svg width="12" height="10" viewBox="0 0 12 10"><rect x="0.5" y="0.5" width="11" height="9" fill="#fff"/><path d="M0.5 0.5 L6 5.5 L11.5 0.5" stroke="#8a6a52" fill="none"/></svg>
  <span class="dot"></span><span class="dot"></span><span class="dot"></span>
</div>
<div class="scroll abs"><span class="bar"></span><span class="label">SCROLL</span></div>

<section class="about abs">
  <div class="eyebrow">About us</div>
  <h1 class="heading">We specialise in the fulfilment of international property developments</h1>
  <div class="photo abs" role="img" aria-label="Photo of a consultant drafting plans at a desk beside a monitor"></div>
  <h2 class="heading who-title">Who we are</h2>
  <p class="who">Corvanta is a consultancy company that helps international property developments fulfil their potential. The company has had great success over the last 10 years of turning around struggling property developments (often resort and investment) and making them reach their maximum potential.</p>
  <h2 class="heading how-title">How we work</h2>
  <p class="how">We work by white labelling or working in-house for each project creating a strategy that is bespoke and unique for each project. It allows a project to purely gain from any initiatives, i.e.. unlike paying agents to promote your project and gain from marketing spend etc..</p>
</section>

<section class="work abs">
  <div class="eyebrow">Our work</div>
  <h2 class="heading lead">We have completed projects in<br><a>Portugal</a>, <a>London</a>, <a>France</a>, <a>Morocco</a>, <a>Brazil</a></h2>

  <article class="project">
    <div class="photo" style="left:117px;top:349px;background:linear-gradient(170deg,#3c4246,#23282b 50%,#8a6a3e 75%,#2a2c2e)" role="img" aria-label="Photo of a lit glass office building on a city corner at dusk">
      <div class="view">View</div>
    </div>
    <div class="info" style="left:609px;top:450px">
      <div class="eyebrow">Featured project</div>
      <h3>Vivendum delicata persequeris ad ius lobortis et qui</h3>
      <div class="place"><svg width="8" height="11" viewBox="0 0 8 11"><path d="M4 0C1.8 0 0 1.7 0 3.9 0 6.8 4 11 4 11s4-4.2 4-7.1C8 1.7 6.2 0 4 0z" fill="#1f5a6c"/></svg>France</div>
      <p>Neglegentur voluptatibus te nam, usu lobortis facilisis consetetur an. Decore molestie at vel. Eum possim facilis volutpat et, quo illud assum assueverit in, habeo noster indoctum vix ea. No mundi propriae ius, vivendum delicata persequeris ad ius. Molestie lobortis et qui.</p>
      <span class="btn">Learn more</span>
    </div>
  </article>

  <article class="project">
    <div class="photo" style="left:691px;top:936px;background:linear-gradient(120deg,#e8e6e6,#a9a7ab 45%,#4a4a4f 70%,#8c7a70)" role="img" aria-label="Photo looking up at a tall grey residential tower"></div>
    <div class="info" style="left:117px;top:1036px">
      <div class="eyebrow">Featured project</div>
      <h3>Utroque invenire reformidans vel id, duo ei case tritani accusam</h3>
      <div class="place"><svg width="8" height="11" viewBox="0 0 8 11"><path d="M4 0C1.8 0 0 1.7 0 3.9 0 6.8 4 11 4 11s4-4.2 4-7.1C8 1.7 6.2 0 4 0z" fill="#1f5a6c"/></svg>London</div>
      <p>Neglegentur voluptatibus te nam, usu lobortis facilisis consetetur an. Decore molestie at vel. Eum possim facilis volutpat et, quo illud assum assueverit in, habeo noster indoctum vix ea. No mundi propriae ius, vivendum delicata persequeris ad ius. Molestie lobortis et qui.</p>
      <span class="btn">Learn more</span>
    </div>
  </article>

  <article class="project">
    <div class="photo" style="left:117px;top:1521px;background:linear-gradient(90deg,#8fc6d9,#b0533b 18%,#a84a33 82%,#7fb9cf)" role="img" aria-label="Photo looking up at a red brick apartment block against a blue sky"></div>
    <div class="info" style="left:609px;top:1622px">
      <div class="eyebrow">Featured project</div>
      <h3>Dicta facete reprimique his adiu placerat vis id</h3>
      <div class="place"><svg width="8" height="11" viewBox="0 0 8 11"><path d="M4 0C1.8 0 0 1.7 0 3.9 0 6.8 4 11 4 11s4-4.2 4-7.1C8 1.7 6.2 0 4 0z" fill="#1f5a6c"/></svg>Morocco</div>
      <p>Neglegentur voluptatibus te nam, usu lobortis facilisis consetetur an. Decore molestie at vel. Eum possim facilis volutpat et, quo illud assum assueverit in, habeo noster indoctum vix ea. No mundi propriae ius, vivendum delicata persequeris ad ius. Molestie lobortis et qui.</p>
      <span class="btn">Learn more</span>
    </div>
  </article>

  <div class="more abs heading">View more work
    <svg width="34" height="24" viewBox="0 0 34 24"><path d="M2 12H31M21 2l10 10-10 10" stroke="#1f5a6c" stroke-width="2.5" fill="none"/></svg>
  </div>
</section>

<footer class="footer abs">
  <nav><span>About us</span><span>Our team</span><span>Projects</span><span>FAQs</span><span>Contact</span></nav>
  <div class="wordmark abs">corvanta.</div>
  <div class="social abs" style="left:31px;top:390px">
    <svg width="12" height="10" viewBox="0 0 12 10"><rect x="0.5" y="0.5" width="11" height="9" fill="#fff"/><path d="M0.5 0.5 L6 5.5 L11.5 0.5" stroke="#14202a" fill="none"/></svg>
    <span class="dot"></span><span class="dot"></span><span class="dot"></span>
  </div>
  <div class="copy abs">© CORVANTA 2020</div>
  <div class="totop abs"><span class="bar"></span><span class="label">Back to top</span></div>
</footer>

</body>
</html>
```